Aerial photo/video drone company needs new business card

Aerial visual company who offers photos and video services via drones.

We are QVL certified and work in the real estate, insurance, construction, and film industries.

I'm looking for a clean, professional, maybe even edgy design, that will be a conversation starter when networking.

I've included our logo, current business card, and font.

Our current business card is decent; albeit, I'm looking for something more unique. If you folks provide good designs, I'll definitely guarantee payment (and I'm not opposed to tipping if the design is above and beyond).

Target Market(s)

Insurance companies, real estate agents, construction companies, advertising & other creative agencies, and filmmakers/producers.

Industry/Entity Type

Business

Contact Information for Business Card

Company name pronounced air-a-vee.

Font styles to use
Other font styles liked:
• Font was uploaded; that or similar; not opposed to other fonts if they work well with the design

Requirements
Must have
• Clearly prominent logo; my name and title; phone number; email address; web address; mentioned "QVL Certified" or similar; should indicate "Aerial visual"
Nice to have
• Watermark of logo or otherwise
Should not have
• Pictures of drones or scenic shots

```html
<!DOCTYPE html>
<html lang="en">
<head>
<meta charset="utf-8">
<title>Orvanta Business Card</title>
<link href="https://fonts.googleapis.com/css2?family=Montserrat:wght@700&family=Open+Sans:wght@400&family=Quicksand:wght@300;400&display=swap" rel="stylesheet">
<style>
  :root {
    --page: #efefef;
    --card: #262626;
    --blue: #1d93c8;
    --label-blue: #1a8ad6;
    --navy: #2d4a7a;
    --white: #ffffff;
  }
  * { margin: 0; padding: 0; box-sizing: border-box; }
  html, body { width: 1200px; height: 1009px; overflow: hidden; background: var(--page); }
  .card {
    position: absolute; left: 100px; top: 205px;
    width: 1000px; height: 600px;
    background: var(--card);
    box-shadow: 0 8px 24px rgba(0,0,0,0.18);
    overflow: hidden;
  }
  .brand-mark {
    position: absolute; right: 60px; top: 50px;
    display: flex; align-items: center; gap: 14px;
  }
  .brand-mark .square { width: 34px; height: 34px; background: var(--blue); }
  .brand-mark .name {
    font-family: 'Quicksand', sans-serif; font-weight: 400;
    font-size: 56px; color: var(--blue); line-height: 1;
  }
  .company {
    position: absolute; left: 60px; top: 95px;
    font-family: 'Montserrat', sans-serif; font-weight: 700;
    font-size: 64px; color: var(--white); letter-spacing: 1px;
  }
  .services {
    position: absolute; left: 66px; top: 178px;
    font-family: 'Open Sans', sans-serif; font-size: 30px; color: var(--blue);
  }
  .certified {
    position: absolute; left: 66px; top: 222px;
    font-family: 'Open Sans', sans-serif; font-size: 30px; color: var(--white);
  }
  .label {
    position: absolute; height: 52px;
    background: var(--label-blue); color: var(--white);
    font-family: 'Quicksand', sans-serif; font-weight: 400;
    font-size: 34px; line-height: 52px; text-align: right; padding-right: 18px;
  }
  .label.telephone { left: 120px; top: 300px; width: 300px; }
  .label.owner { left: 220px; top: 362px; width: 200px; }
  .label.email { left: 290px; top: 424px; width: 130px; }
  .detail {
    position: absolute; left: 470px;
    font-family: 'Quicksand', sans-serif; font-weight: 300;
    font-size: 32px; color: var(--white); letter-spacing: 1px; line-height: 52px;
  }
  .detail.phone { top: 300px; }
  .detail.person { top: 362px; letter-spacing: 3px; }
  .detail.mail { top: 424px; }
  .website {
    position: absolute; left: 250px; top: 486px;
    font-family: 'Quicksand', sans-serif; font-weight: 400;
    font-size: 32px; color: var(--blue); letter-spacing: 3px;
  }
  .footer-band {
    position: absolute; left: 0; bottom: 0; width: 100%; height: 62px;
    background: var(--blue);
  }
</style>
</head>
<body>
  <div class="card">
    <div class="brand-mark">
      <span class="square"></span>
      <span class="name">orvanta</span>
    </div>
    <div class="company">ORVANTA</div>
    <div class="services">Film , insurance, Construction</div>
    <div class="certified">QVL Certified</div>

    <div class="label telephone">TELEPHONE</div>
    <div class="label owner">OWNER</div>
    <div class="label email">EMAIL</div>

    <div class="detail phone">555.014.2290</div>
    <div class="detail person">Daniel K.Morrow</div>
    <div class="detail mail">dan@orvanta.com</div>

    <div class="website">orvanta.com</div>
    <div class="footer-band"></div>
  </div>
</body>
</html>
```